Investment company needing business card

We are wanting a business card which looks sharp and easy on the eye. We are thinking of having a business card with the logo embossed on it, to really make it stand out. We will only have a small amount of information of the business card, person's name, position, email address and phone number

Contact Information for Business Card

Danica Pruett
Executive Assistant
+64 21 547 3162
danicap@harwellcapital.co.nz

Requirements
Must have
• Embossed logo
Should not have
• Not to be busy

```html
<!DOCTYPE html>
<html lang="en">
<head>
<meta charset="utf-8">
<title>Harwell Capital – Business Card</title>
<link href="https://fonts.googleapis.com/css2?family=Roboto:wght@700&family=Arimo:wght@400&display=swap" rel="stylesheet">
<style>
  :root {
    --backdrop: #d6d6d6;
    --card-white: #ffffff;
    --brand-green: #41ff41;
    --brand-slate: #566362;
    --text-light: #ffffff;
  }
  * { margin: 0; padding: 0; box-sizing: border-box; }
  html, body {
    width: 1200px;
    height: 1000px;
    overflow: hidden;
    background: var(--backdrop);
  }
  .business-card {
    position: absolute;
    left: 180px;
    top: 260px;
    width: 840px;
    height: 480px;
    display: flex;
    flex-direction: column;
  }
  .card-brand {
    height: 240px;
    background: var(--card-white);
    display: flex;
    align-items: center;
    justify-content: center;
    gap: 22px;
  }
  .brand-square {
    width: 100px;
    height: 100px;
    background: var(--brand-slate);
    border-radius: 14px;
  }
  .brand-name {
    font-family: "Roboto", sans-serif;
    font-weight: 700;
    font-size: 38px;
    letter-spacing: 0.5px;
    color: var(--brand-green);
    text-transform: uppercase;
  }
  .card-details {
    height: 240px;
    background: var(--brand-green);
    color: var(--text-light);
    text-align: center;
    padding-top: 38px;
  }
  .person-name {
    font-family: "Roboto", sans-serif;
    font-weight: 700;
    font-size: 44px;
    line-height: 50px;
  }
  .person-role {
    font-family: "Arimo", sans-serif;
    font-size: 22px;
    letter-spacing: 1px;
    line-height: 26px;
  }
  .contact-phone {
    font-family: "Arimo", sans-serif;
    font-size: 28px;
    letter-spacing: 1.5px;
    margin-top: 18px;
    line-height: 34px;
  }
  .contact-email {
    font-family: "Arimo", sans-serif;
    font-size: 26px;
    letter-spacing: 1px;
    margin-top: 6px;
    line-height: 32px;
  }
</style>
</head>
<body>
  <div class="business-card">
    <header class="card-brand">
      <span class="brand-square" aria-hidden="true"></span>
      <span class="brand-name">Harwell Capital</span>
    </header>
    <section class="card-details">
      <p class="person-name">Danica Pruett</p>
      <p class="person-role">executive assistant</p>
      <p class="contact-phone">+64 21 547 3162</p>
      <p class="contact-email">danicap@harwellcapital.co.nz</p>
    </section>
  </div>
</body>
</html>
```